Dale Hornsby's Swingcraft Big Band — Hot & Sticky ------ CD Cover Art (and Disc Art)

Need a front cover jacket and a disc design for a fantastic all-pro big band (jazz/funk/reggae) CD. We really want to use a group photo somehow since so many of the band members are world famous, LA's finest studio musicians with mostly original music arranged by the biggest names in jazz. Playful, fun, lighthearted, tasteful arrangements with world class soloists.

Target Market(s)

Music/Jazz/Big band enthusiasts; other musicians

Other font styles liked:
• See uploaded file #4

Colors

Designer to choose colors to be used in the design.

Requirements
Must have
• Legibility . . . must be easy to read and not crowded or cluttered. Font idea below (A Quiet Night Beneath The Tangled Pines) is for feel and flavor. It is absolutely not necessary to match if you have something you like better.
Nice to have
• Colorful but not tacky. Maybe a play on the CD title, Hot and Sticky?

```html
<!DOCTYPE html>
<html lang="en">
<head>
<meta charset="utf-8">
<title>Dale Hornsby's Swingcraft Big Band — Hot and Sticky</title>
<link rel="stylesheet" href="https://fonts.googleapis.com/css2?family=Arimo:wght@700&family=Titan+One&display=swap">
<style>
  :root {
    --sky-pale: #cfe6e7;
    --sky-mid: #b9d6d8;
    --sky-deep: #8fb0b4;
    --panel: #d3e9ea;
    --ink-slate: #5e6a6f;
    --ink-black: #111111;
    --letter-fill: #ffffff;
  }
  html, body {
    margin: 0;
    padding: 0;
    width: 1200px;
    height: 1200px;
    overflow: hidden;
    background: var(--sky-pale);
  }
  .cover {
    position: relative;
    width: 1200px;
    height: 1200px;
    overflow: hidden;
  }
  .cover-backdrop {
    position: absolute;
    inset: 0;
    background:
      radial-gradient(ellipse at 50% 50%, var(--sky-pale) 0%, var(--sky-mid) 70%, var(--sky-deep) 100%);
  }
  .title-panel {
    position: absolute;
    left: 280px;
    top: 360px;
    width: 652px;
    height: 652px;
    background: linear-gradient(160deg, #d9eeef 0%, var(--panel) 60%, #c6dfe1 100%);
    box-shadow: 0 0 28px rgba(90, 120, 125, 0.35);
  }
  .band-name {
    position: absolute;
    left: 0;
    top: 0;
    width: 1200px;
    height: 340px;
  }
  .band-name text {
    font-family: "Arimo", Arial, sans-serif;
    font-weight: 700;
    fill: var(--ink-slate);
    text-anchor: middle;
  }
  .album-title {
    position: absolute;
    left: 0;
    top: 0;
    width: 1200px;
    height: 1200px;
  }
  .album-title text {
    font-family: "Titan One", "Arial Black", sans-serif;
    fill: var(--letter-fill);
    stroke: var(--ink-black);
    stroke-width: 3px;
    paint-order: stroke;
    text-anchor: middle;
  }
  .label-mark {
    position: absolute;
    left: 74px;
    top: 1080px;
    display: flex;
    align-items: center;
    gap: 10px;
    font-family: "Arimo", Arial, sans-serif;
    font-weight: 700;
    font-size: 26px;
    line-height: 1.1;
    color: var(--ink-black);
  }
  .label-mark__square {
    width: 18px;
    height: 18px;
    background: var(--ink-black);
  }
  .label-mark__name {
    display: flex;
    flex-direction: column;
  }
</style>
</head>
<body>
  <main class="cover">
    <div class="cover-backdrop" role="img" aria-label="Pale blue distressed background with faint handwritten sheet music and scratched texture"></div>

    <svg class="band-name" viewBox="0 0 1200 340" role="heading" aria-level="1" aria-label="Dale Hornsby's Swingcraft Big Band">
      <text x="606" y="188" font-size="96" textLength="1060" lengthAdjust="spacingAndGlyphs">DALE HORNSBY'S SWINGCRAFT</text>
      <text x="604" y="308" font-size="94" textLength="424" lengthAdjust="spacingAndGlyphs">BIG BAND</text>
    </svg>

    <div class="title-panel" role="img" aria-label="Lighter square panel with faint sheet music texture"></div>

    <svg class="album-title" viewBox="0 0 1200 1200" aria-label="Hot and Sticky">
      <text x="606" y="608" font-size="150" textLength="420" lengthAdjust="spacingAndGlyphs">HOT</text>
      <text x="592" y="712" font-size="70" textLength="146" lengthAdjust="spacingAndGlyphs">AND</text>
      <text x="606" y="880" font-size="150" textLength="424" lengthAdjust="spacingAndGlyphs">STICKY</text>
    </svg>

    <div class="label-mark">
      <span class="label-mark__square"></span>
      <span class="label-mark__name"><span>TALL PINE</span><span>RECORDS</span></span>
    </div>
  </main>
</body>
</html>
```